Business Card Redesign

We would like to redesign our existing business cards.
The new design shall look:
ELEGANT, LUXURY, PROFESSIONAL
Reference:
YOU CAN VISIT WWW.LUMEN-BRIDGE-PARTNERS.EXAMPLE FOR BETTER UNDERSTANDING OF COMPANY STRATEGY AND POSITION
Additional:
CHOSEN CANDIDATE SHALL PROVIDE THE INSTRUCTION OF PRINTING IF ANY THERMAL COVERAGE OR ANY ADDITION IS OFFERED
Industry/Entity Type
Business

```html
<!DOCTYPE html>
<html lang="en">
<head>
<meta charset="utf-8">
<title>Lumen Bridge Partners – Business Card</title>
<link href="https://fonts.googleapis.com/css2?family=Open+Sans:wght@400;600;700&family=Oswald:wght@500&display=swap" rel="stylesheet">
<style>
  :root {
    --navy: #2e4a94;
    --navy-deep: #243d80;
    --gold: #e2a82a;
    --ink: #555a63;
    --paper: #ffffff;
    --backdrop: #ebe8e2;
  }
  html, body {
    margin: 0;
    width: 1200px;
    height: 675px;
    overflow: hidden;
    background: var(--backdrop);
    font-family: "Open Sans", Arial, sans-serif;
  }
  .card {
    position: absolute;
    left: 150px;
    top: 80px;
    width: 900px;
    height: 514px;
    background: var(--paper);
    box-shadow: 0 10px 30px rgba(0,0,0,.18);
    overflow: hidden;
  }
  .card-art { position: absolute; inset: 0; }
  .holder {
    position: absolute;
    right: 470px;
    top: 140px;
    text-align: right;
  }
  .holder-name {
    font-family: "Oswald", "Arial Narrow", sans-serif;
    font-weight: 500;
    font-size: 36px;
    letter-spacing: 1px;
    color: var(--navy);
    margin: 0;
    line-height: 1.1;
  }
  .holder-role {
    font-size: 18px;
    color: var(--gold);
    margin: 2px 0 0;
  }
  .divider {
    position: absolute;
    left: 455px;
    top: 45px;
    width: 1px;
    height: 215px;
    background: #d9dbe0;
  }
  .company {
    position: absolute;
    left: 478px;
    top: 48px;
    color: var(--ink);
    font-size: 16px;
    line-height: 1.4;
  }
  .company-name {
    color: var(--gold);
    font-weight: 700;
    font-size: 20px;
    margin: 0 0 2px;
  }
  .address { margin: 0 0 14px; }
  .contacts { list-style: none; margin: 0; padding: 0; font-size: 15px; }
  .contacts li { display: flex; align-items: center; gap: 8px; line-height: 1.5; }
  .contacts svg { width: 14px; height: 14px; flex: none; }
  .brand {
    position: absolute;
    left: 48px;
    top: 300px;
    display: flex;
    align-items: center;
    gap: 14px;
  }
  .brand-dot {
    width: 64px;
    height: 64px;
    border-radius: 50%;
    background: var(--navy);
  }
  .brand-name {
    font-weight: 700;
    font-size: 22px;
    letter-spacing: 1px;
    color: var(--navy);
  }
  .web {
    position: absolute;
    left: 50px;
    top: 455px;
    font-size: 18px;
    font-weight: 600;
    color: var(--gold);
    letter-spacing: .5px;
  }
</style>
</head>
<body>
  <article class="card">
    <svg class="card-art" viewBox="0 0 900 514" aria-hidden="true">
      <path d="M560 514 C690 420 800 300 900 175 L900 205 C800 320 700 430 600 514Z" fill="var(--gold)"/>
      <path d="M520 514 C660 410 790 290 900 150 L900 156 C790 298 665 416 528 514Z" fill="var(--gold)"/>
      <path d="M0 420 C250 415 520 390 700 320 C790 285 850 250 900 220 L900 514 L0 514Z" fill="var(--navy)"/>
      <path d="M0 420 C250 415 520 390 700 320 C790 285 850 250 900 220 L900 226 C850 256 790 292 700 327 C520 397 250 422 0 426Z" fill="var(--gold)"/>
      <path d="M0 500 C200 498 380 492 520 480 L520 514 L0 514Z" fill="var(--navy-deep)"/>
    </svg>

    <div class="brand">
      <span class="brand-dot"></span>
      <span class="brand-name">LUMEN BRIDGE</span>
    </div>

    <div class="holder">
      <h1 class="holder-name">MIRA SOLEN</h1>
      <p class="holder-role">PR Consultant</p>
    </div>

    <div class="divider"></div>

    <section class="company">
      <h2 class="company-name">Lumen Bridge Partners Ltd</h2>
      <p class="address">Headquarters (Hong Kong)<br>Rm.1208B,12/F, Harbourline Tower<br>18 Lantern Street, Central</p>
      <ul class="contacts">
        <li>
          <svg viewBox="0 0 14 14"><rect x="1" y="3" width="12" height="8" fill="var(--navy)"/><path d="M1 3 L7 8 L13 3" stroke="#fff" stroke-width="1.2" fill="none"/></svg>
          mira@lumen-bridge-partners.example
        </li>
        <li>
          <svg viewBox="0 0 14 14"><rect x="4" y="1" width="6" height="12" rx="1" fill="var(--navy)"/><rect x="5" y="2.5" width="4" height="7" fill="#fff"/></svg>
          (852) 5550 0142
        </li>
        <li>
          <svg viewBox="0 0 14 14"><path d="M3 1 L6 4 L4.5 6 C5.5 8 6 8.5 8 9.5 L10 8 L13 11 L11 13 C6 12 2 8 1 3Z" fill="var(--navy)"/></svg>
          (852) 5550 0187
        </li>
        <li>
          <svg viewBox="0 0 14 14"><rect x="3" y="1" width="8" height="4" fill="var(--navy)"/><rect x="1" y="5" width="12" height="5" fill="var(--navy)"/><rect x="3" y="9" width="8" height="4" fill="var(--navy)" stroke="#fff" stroke-width="1"/></svg>
          (852) 5550 0199
        </li>
      </ul>
    </section>

    <p class="web" style="margin:0">www.lumen-bridge-partners.example</p>
  </article>
</body>
</html>
```